Business Card Design Project

We need a business card design for a new boutique consulting company, LumaConsulting. Our new logo has just been designed and we are looking for simple, clean looking business cards. Logo attached

Industry/Entity Type

Boutique

Requirements
Must have
• There must be room for each card to have the following details:
Name
Title
Address - 2 lines
Phone number
Email address
Website address

Nice to have
• May have something on the back of the buisness card - emphasing the word "Luma".

```html
<!DOCTYPE html>
<html lang="en">
<head>
<meta charset="utf-8">
<title>LumaConsulting Business Card</title>
<link href="https://fonts.googleapis.com/css2?family=Merriweather:ital,wght@0,300;0,400;0,700;1,400;1,700&display=swap" rel="stylesheet">
<style>
  :root {
    --canvas: #ffffff;
    --bleed: #cbcbcb;
    --paper: #ffffff;
    --brand-green: #7dc242;
    --text-grey: #a7a7a7;
    --title-grey: #9d9d9d;
    --guide: #555555;
    --shadow: rgba(0, 0, 0, 0.35);
  }
  * { margin: 0; padding: 0; box-sizing: border-box; }
  html, body {
    width: 1200px;
    height: 900px;
    overflow: hidden;
    background: var(--canvas);
    font-family: "Merriweather", Georgia, serif;
  }
  .canvas { position: relative; width: 1200px; height: 900px; }

  .card {
    position: absolute;
    left: 267px;
    width: 664px;
    height: 322px;
    background: var(--bleed);
    box-shadow: 4px 4px 5px var(--shadow);
  }
  .card--front { top: 101px; }
  .card--back { top: 472px; }

  .card__trim {
    position: absolute;
    left: 15px; top: 13px; right: 15px; bottom: 13px;
    background: var(--paper);
    border: 1px dotted var(--guide);
  }
  .card__frame {
    position: absolute;
    left: 14px; top: 9px; right: 13px; bottom: 10px;
    border: 1px solid var(--brand-green);
  }

  .wordmark {
    position: absolute;
    display: flex;
    align-items: center;
    gap: 6px;
    color: var(--brand-green);
    font-weight: 400;
    white-space: nowrap;
    letter-spacing: -0.3px;
  }
  .wordmark__dot {
    display: inline-block;
    background: var(--text-grey);
  }
  .card--front .wordmark { left: 51px; top: 141px; font-size: 22px; }
  .card--front .wordmark__dot { width: 14px; height: 14px; }
  .card--back .wordmark { left: 0; right: 0; top: 159px; justify-content: center; font-size: 34px; }
  .card--back .wordmark__dot { width: 22px; height: 22px; }

  .divider {
    position: absolute;
    left: 290px; top: 20px;
    width: 1px; height: 238px;
    background: var(--brand-green);
  }

  .contact {
    position: absolute;
    right: 36px; top: 52px;
    text-align: right;
    font-size: 14.5px;
    line-height: 19px;
    color: var(--text-grey);
    font-weight: 300;
  }
  .contact__name { color: var(--brand-green); font-size: 17.5px; font-weight: 300; line-height: 20px; }
  .contact__title { color: var(--title-grey); font-style: italic; font-weight: 700; font-size: 14px; line-height: 18px; }
  .contact__address { margin-top: 12px; }
  .contact__phone { margin-top: 11px; }
  .contact__email { margin-top: 17px; font-weight: 700; color: var(--title-grey); line-height: 17px; }
  .contact__web { color: var(--brand-green); font-style: italic; line-height: 17px; }
</style>
</head>
<body>
<main class="canvas">
  <section class="card card--front" aria-label="Card front">
    <div class="card__trim">
      <div class="card__frame">
        <div class="wordmark"><span class="wordmark__dot"></span>LumaConsulting</div>
        <div class="divider"></div>
        <div class="contact">
          <p class="contact__name">Daniel Hart</p>
          <p class="contact__title">Operations Manager</p>
          <p class="contact__address">48 Orchard Lane<br>Riverton, State</p>
          <p class="contact__phone">321 555 0178</p>
          <p class="contact__email">hart@lumaconsulting.com</p>
          <p class="contact__web">www.lumaconsulting.com</p>
        </div>
      </div>
    </div>
  </section>

  <section class="card card--back" aria-label="Card back">
    <div class="card__trim">
      <div class="card__frame">
        <div class="wordmark"><span class="wordmark__dot"></span>LumaConsulting</div>
      </div>
    </div>
  </section>
</main>
</body>
</html>
```